Digital Album Cover - Piano music for wedding ceremonies and receptions

I need cover art for a piano album project that will be distributed to TuneVault, Wavelane etc. Covert art required for front of album. At this stage physical CDs will not be printed nor required it is just a digital release.
Artist name: Toby Hargrove
Album Title: Gentle Keys Melodies Wedding Ceremonies and Receptions
Volume 3
Sample piano songs are on my tunecast page
https://tunecast.example/tobyhargrovekeys/sets/gentle-keys-melodies-vol-3
Previous album artwork used from sketch hive competitions winners
https://musicvault.example/au/artist/toby-hargrove/4830917265
Target Market(s)
brides to be
grooms to be
people interested in weddings
people enjoy love songs or easy listening music
Industry/Entity Type
Wedding
Look and feel
Each slider illustrates characteristics of the customer's brand and the style your logo design should communicate.

```html
<!DOCTYPE html>
<html lang="en">
<head>
<meta charset="utf-8">
<title>Toby Hargrove – Gentle Keys Melodies, Volume 3</title>
<link rel="stylesheet" href="https://fonts.googleapis.com/css2?family=Oswald:wght@300;600&family=Tulpen+One&family=Roboto+Condensed:wght@400&display=swap">
<style>
  :root {
    --stage: #d9d9d9;
    --cover-black: #050202;
    --deep-red: #3a0604;
    --glow-red: #8e1a10;
    --accent-red: #c0392b;
    --ink-white: #f4f0ee;
  }
  html, body {
    margin: 0;
    width: 1200px;
    height: 1200px;
    overflow: hidden;
    background: var(--stage);
  }
  .album-cover {
    position: absolute;
    left: 100px;
    top: 100px;
    width: 1000px;
    height: 1000px;
    background: var(--cover-black);
    overflow: hidden;
  }
  .cover-photo {
    position: absolute;
    inset: 0;
    background:
      radial-gradient(ellipse 30% 45% at 30% 40%, rgba(142,26,16,0.85), transparent 70%),
      radial-gradient(ellipse 40% 30% at 55% 85%, rgba(110,18,10,0.7), transparent 75%),
      radial-gradient(ellipse 25% 30% at 35% 12%, rgba(160,40,25,0.55), transparent 70%),
      linear-gradient(160deg, var(--deep-red) 0%, var(--cover-black) 60%, #1a0302 100%);
  }
  .volume-label {
    position: absolute;
    top: 42px;
    right: 48px;
    margin: 0;
    font-family: "Oswald", sans-serif;
    font-weight: 300;
    font-size: 34px;
    color: var(--ink-white);
    letter-spacing: 1px;
  }
  .album-title {
    position: absolute;
    left: 365px;
    top: 408px;
    margin: 0;
    font-family: "Oswald", sans-serif;
    font-weight: 600;
    font-size: 34px;
    line-height: 1.2;
    color: var(--ink-white);
    text-transform: uppercase;
    letter-spacing: 0.5px;
  }
  .artist-name {
    position: absolute;
    left: 458px;
    top: 470px;
    width: 492px;
    height: 240px;
    overflow: visible;
  }
  .artist-name text {
    font-family: "Tulpen One", sans-serif;
    font-size: 200px;
    fill: var(--accent-red);
  }
  .title-rule {
    position: absolute;
    left: 460px;
    top: 727px;
    width: 486px;
    height: 2px;
    background: var(--accent-red);
  }
  .album-subtitle {
    position: absolute;
    right: 54px;
    top: 740px;
    margin: 0;
    font-family: "Roboto Condensed", sans-serif;
    font-size: 22px;
    color: var(--ink-white);
  }
</style>
</head>
<body>
  <main class="album-cover">
    <div class="cover-photo" role="img" aria-label="Silhouette of a bride and groom embracing before a window, bathed in red light, her long veil trailing over piano keys"></div>
    <p class="volume-label">Volume 3</p>
    <h1 class="album-title">Gentle Keys Melodies</h1>
    <svg class="artist-name" viewBox="0 0 492 240" aria-label="Toby Hargrove">
      <text x="2" y="205" textLength="486" lengthAdjust="spacingAndGlyphs">Toby Hargrove</text>
    </svg>
    <div class="title-rule"></div>
    <p class="album-subtitle">Wedding ceremonies and receptions</p>
  </main>
</body>
</html>
```